New Business Card Design Project

We require a business card design for Pharvelix, a newly established Indian company.
Our focus is on the development, manufacturing, and export of a diverse array of pharmaceutical products on a global scale. The card should convey a professional appearance, as our primary markets are in Africa, China, and Southeast Asian nations.
We envision a two-sided business card, with the reverse side dedicated to a logo set against a solid color or an elegantly designed pattern. The corners should be rounded. We would appreciate seeing both horizontal and vertical design options. We trust the designer to utilize their expertise in creating this design.

The content for the business card is included in the attached Word file.

Target Market(s)

Our primary markets are in Africa, China, and Southeast Asian, Latin America, Maldives, Sri Lanka

Industry/Entity Type

Pharmaceutical Manufacturing and Export

Contact Information for Business Card

Colors

Designer to choose colors to be used in the design.

Requirements
Must have
• The reverse side of the business card features solely the logo along with the tagline, "Care for Every Life."
Should not have
• The logo should not exceed two instances, encompassing both the front and back sides of the card.

```html
<!DOCTYPE html>
<html lang="en">
<head>
<meta charset="utf-8">
<title>Pharvelix Business Card</title>
<link rel="stylesheet" href="https://fonts.googleapis.com/css2?family=Montserrat:wght@400;500;600&display=swap">
<style>
  :root {
    --brand-blue: #29a7df;
    --brand-red: #ee5f4b;
    --ink-grey: #5e5e5e;
    --card-white: #ffffff;
    --stage: #2e2e2e;
  }
  * { margin: 0; padding: 0; box-sizing: border-box; }
  html, body { width: 1200px; height: 987px; overflow: hidden; }
  body {
    background: var(--stage);
    font-family: "Montserrat", sans-serif;
    position: relative;
  }
  .card {
    position: absolute;
    width: 640px;
    height: 366px;
    border-radius: 14px;
    overflow: hidden;
  }
  /* Reverse side */
  .card-back {
    left: 110px;
    top: 110px;
    background: var(--brand-blue);
  }
  .back-pattern {
    position: absolute;
    inset: 0;
    background: linear-gradient(135deg, #2eaee4 0%, #2aa6de 50%, #259fd8 100%);
  }
  .back-brand {
    position: absolute;
    left: 0; right: 0;
    top: 142px;
    display: flex;
    align-items: center;
    justify-content: center;
    gap: 14px;
  }
  .brand-dot {
    width: 22px; height: 22px;
    border-radius: 50%;
    flex: none;
  }
  .back-brand .brand-dot { background: var(--card-white); }
  .back-brand .brand-name {
    color: var(--card-white);
    font-weight: 600;
    font-size: 50px;
    letter-spacing: 0.5px;
  }
  .tagline {
    position: absolute;
    left: 0; right: 0;
    bottom: 58px;
    text-align: center;
    color: var(--card-white);
    font-weight: 500;
    font-size: 15px;
    letter-spacing: 0.8px;
  }
  /* Front side */
  .card-front {
    left: 450px;
    top: 500px;
    background: var(--card-white);
  }
  .front-brand {
    position: absolute;
    left: 40px;
    top: 168px;
    display: flex;
    align-items: center;
    gap: 12px;
  }
  .front-brand .brand-dot { background: var(--brand-red); width: 18px; height: 18px; }
  .front-brand .brand-name {
    color: var(--brand-blue);
    font-weight: 600;
    font-size: 42px;
  }
  .divider {
    position: absolute;
    left: 322px;
    top: 80px;
    width: 2px;
    height: 170px;
    background: var(--brand-red);
  }
  .contact {
    position: absolute;
    left: 346px;
    top: 76px;
    color: var(--ink-grey);
  }
  .person-name {
    color: var(--brand-blue);
    font-weight: 600;
    font-size: 22px;
  }
  .person-role { font-size: 15px; margin-top: 2px; }
  .address { font-size: 14px; line-height: 1.3; margin-top: 14px; }
  .contact-list { list-style: none; margin-top: 12px; font-size: 15px; line-height: 1.45; }
  .contact-list li { display: flex; align-items: center; gap: 8px; }
  .contact-list svg { width: 13px; height: 13px; flex: none; }
  .front-waves { position: absolute; left: 0; bottom: 0; width: 640px; height: 140px; }
</style>
</head>
<body>

<section class="card card-back" aria-label="Card reverse side">
  <div class="back-pattern" role="img" aria-label="Subtle repeating brand pattern in lighter blue"></div>
  <div class="back-brand">
    <span class="brand-dot"></span>
    <span class="brand-name">Pharvelix</span>
  </div>
  <p class="tagline">Care for Every Life.</p>
</section>

<section class="card card-front" aria-label="Card front side">
  <div class="front-brand">
    <span class="brand-dot"></span>
    <span class="brand-name">Pharvelix</span>
  </div>
  <div class="divider"></div>
  <div class="contact">
    <p class="person-name">Arjun K. Malvade</p>
    <p class="person-role">CEO</p>
    <p class="address">12, Sunflower Colony, Nashik<br>422003, India</p>
    <ul class="contact-list">
      <li>
        <svg viewBox="0 0 12 12" fill="none" stroke="#ee5f4b" stroke-width="1.4"><rect x="3" y="0.8" width="6" height="10.4" rx="1"/><line x1="5.3" y1="9.3" x2="6.7" y2="9.3"/></svg>
        +919812345670
      </li>
      <li>
        <svg viewBox="0 0 12 12"><rect x="0.5" y="2" width="11" height="8" fill="#ee5f4b"/><path d="M0.5 2 L6 6.5 L11.5 2" fill="none" stroke="#fff" stroke-width="1"/></svg>
        amalvade@pharvelix.com
      </li>
      <li>
        <svg viewBox="0 0 12 12" fill="none" stroke="#ee5f4b" stroke-width="1"><circle cx="6" cy="6" r="5.2"/><ellipse cx="6" cy="6" rx="2.2" ry="5.2"/><line x1="0.8" y1="6" x2="11.2" y2="6"/><line x1="1.6" y1="3.4" x2="10.4" y2="3.4"/><line x1="1.6" y1="8.6" x2="10.4" y2="8.6"/></svg>
        pharvelix.com
      </li>
    </ul>
  </div>
  <svg class="front-waves" viewBox="0 0 640 140" preserveAspectRatio="none" aria-hidden="true">
    <path d="M400 64 C500 54 580 30 640 6 L640 18 C580 42 500 60 400 64 Z" fill="#29a7df"/>
    <path d="M0 78 C260 80 480 66 640 32 L640 140 L0 140 Z" fill="#ee5f4b"/>
  </svg>
</section>

</body>
</html>
```